USA Home and Kitchen "Multi-Product" Brand Needs a Stunning Packaging Design.

We need a new packaging design for our Brand: T&M Hearth & Nest. We Manufacture, Market, and Sell Home & Kitchen Products (Such as Kitchen Utensils and Home Decor to name a few) Direct to Consumers in the United States via our Website and Vendora.com. We would like to see designs that are simple, clean, and modern, yet stand out and demand attention. Our Preferred colors of the design should include: Black or Grey as the base color/shade), White or Grey for the text, and some additional color can be used for complementary elements/visuals at your own discretion or creativity. We would like this to be an Interchangeable Design that can be easily modified and implemented across all of our other products (i.e: does not contain too many images or design elements that reference a particular product.

Although this design and the concept as a whole is intended to be used across our entire catalogue of products. Please feel free to base your design on our one of our top selling products as per the following URL: https://www.vendora-shop.example/dp/X93QL4471Z?ref=abc_item_dp.

Target Market(s)

Our customers tend come from many areas across the spectrum. But the quintessential T&M target customer (the type of person who tends to be our most receptive and loyal customer) is female and part of the Millennials generation, aged in her 30s, and is either working full-time in a white-collar job or on home duties, of which she would have young children, a spouse, or other family members to look after. She’s part of the conventional family life who represent the core of ‘middle America’. She doesn’t mind to splurge every now and again on shopping for items that she wants and/or needs, whilst some of the time she’ll also go out of her way to ‘search for a bargain’. She tends to spend more time in her home and kitchen than the average individual. We recognize that cooking for herself and family, and providing a well furnished and stylish home is part of who she is.

Industry/Entity Type

Retail

Font styles to use
Serif
Sans Serif

Colors

Designer to choose only greyscale colors for use in the design.

Requirements
Must have
• Interchangeable Design (A "Universal" Packaging Design that can be easily modified and adapted for use with a large catalogue of products under our brand).
Nice to have
• Some visual elements that gives our packaging/brand the ability to stand out and be unique/memorable.
Should not have
• Our design should not have too much text. Nor should it be cluttered or overcrowded with too much information or visual elements. And does not contain too many images or design elements that reference a particular product. We believe simplicity is key, and quality over quantity.

```html
<!DOCTYPE html>
<html lang="en">
<head>
<meta charset="utf-8">
<title>T&amp;M Hearth &amp; Nest — Pie Server Packaging</title>
<link href="https://fonts.googleapis.com/css2?family=Marcellus&display=swap" rel="stylesheet">
<style>
  :root {
    --backdrop: #e4e4e4;
    --box-top: #141414;
    --box-bottom: #0a0a0a;
    --box-edge: #2c2c2c;
    --silver: #a8a8aa;
    --wave-bright: #14aee8;
    --wave-deep: #0b3a52;
  }
  * { margin: 0; padding: 0; box-sizing: border-box; }
  html, body {
    width: 1200px;
    height: 1200px;
    overflow: hidden;
    background: var(--backdrop);
  }
  .canvas {
    position: relative;
    width: 1200px;
    height: 1200px;
  }
  .box-front {
    position: absolute;
    left: 442px;
    top: 50px;
    width: 316px;
    height: 1100px;
    background: linear-gradient(180deg, var(--box-top), var(--box-bottom));
    border: 3px solid var(--box-edge);
    font-family: "Marcellus", sans-serif;
    color: var(--silver);
    text-align: center;
  }
  .brand {
    position: absolute;
    top: 86px;
    left: 0;
    right: 0;
  }
  .brand-name {
    display: block;
    font-size: 50px;
    line-height: 1;
    letter-spacing: 1px;
  }
  .brand-sub {
    display: block;
    margin-top: 8px;
    font-size: 9px;
    letter-spacing: 1.6px;
    text-transform: uppercase;
  }
  .product-title {
    position: absolute;
    top: 278px;
    left: 0;
    right: 0;
    font-size: 58px;
    font-weight: 400;
    line-height: 66px;
    letter-spacing: 1px;
  }
  .wave-band {
    position: absolute;
    top: 508px;
    left: 0;
    right: 0;
    height: 314px;
    background:
      linear-gradient(172deg, transparent 0%, transparent 18%, rgba(20,174,232,0.55) 34%, rgba(11,58,82,0.85) 55%, rgba(20,174,232,0.6) 78%, transparent 96%);
  }
  .product-tagline {
    position: absolute;
    top: 952px;
    left: 0;
    right: 0;
    font-size: 24px;
    line-height: 33px;
  }
</style>
</head>
<body>
  <main class="canvas">
    <section class="box-front">
      <div class="brand">
        <span class="brand-name">T&amp;M</span>
        <span class="brand-sub">Hearth &amp; Nest</span>
      </div>
      <h1 class="product-title">PIE<br>SERVER</h1>
      <div class="wave-band" role="img" aria-label="Flowing bundle of thin bright blue wave lines sweeping across the box"></div>
      <p class="product-tagline">cut and serve<br>spatula</p>
    </section>
  </main>
</body>
</html>
```